Federal IT Consulting Company - Corvalen Advisory Partners

We're seeking a skilled web designer to create a modern, bold, and engaging WordPress website for Corvalen Advisory Partners, LLC. Our company specializes in federal IT consulting, and our name is a play on "Charting Circuitry." The website should reflect our expertise in the federal technology marketplace and position us as a trusted partner for clients navigating their IT journey.

contact: info@corvalenadv.example

Current Status

WordPress is already installed on our hosting account
We have an existing logo (may need modernization)

Design Requirements

Style:

Modern and visually striking design
Bold elements to convey confidence and expertise
Incorporate the concept of "charting circuitry" into the design

Features:

Modern UX sliders for dynamic content presentation
Eye-catching, high-quality images (stock photos to be sourced by the designer)
Responsive design for all devices

Color Scheme:

To be proposed by the designer, should align with our brand and convey trust and technological expertise

Logo:

Evaluate our current logo
Create a transparent background version if needed
Propose modernization if deemed necessary

Accessibility:

Ensure design elements are accessible to users with disabilities
Use high contrast ratios for text and background colors
Provide text alternatives for non-text content

Website Structure
Create the following pages, with the possibility of subpages:

Home
Services
About
Contact

Specific Page Requirements
Home Page

Striking hero section with a clear value proposition
Overview of our services
Client testimonials or trust indicators

Services Page

Detailed list of our IT consulting services
Clear explanation of how we help navigate the federal IT landscape

About Page

Company history and mission
Team highlights (if applicable)
Our approach to federal IT consulting

Contact Page

Contact form
Other contact methods (phone, email)

Technical Requirements

Fully responsive design
SEO best practices implemented
Fast loading times
Integration with necessary plugins (to be discussed)
Training on how to update and maintain the site
Full compliance with Web Content Accessibility Guidelines (WCAG) 2.1 Level AA
Adherence to Section 508 standards for federal website accessibility
Implementation of necessary features for ADA compliance

Target Market(s)

US Federal Govt customers looking for IT support.

Industry/Entity Type

IT Consulting

Coding

Coded - Design and coding required

Colors
0054AA
0677BA
7BADD7
CADEEF
E8F1F8
0094D4
00A9DD
6FCCEA
C7EBF8
E9F6FB
00AB8E
00BBA5
67D7C9
C6EFE9
E9F9F6

```html
<!DOCTYPE html>
<html lang="en">
<head>
<meta charset="utf-8">
<title>Corvalen Advisory Partners</title>
<link href="https://fonts.googleapis.com/css2?family=Poppins:wght@400;500;600;700;800&display=swap" rel="stylesheet">
<style>
:root{
  --blue:#0054AA;
  --blue-mid:#0677BA;
  --blue-light:#7BADD7;
  --sky:#00A9DD;
  --navy:#0A2478;
  --ink:#1d1d1f;
  --muted:#6b6f76;
  --pale:#eef0f3;
  --white:#ffffff;
  --star:#f08a24;
}
*{margin:0;padding:0;box-sizing:border-box}
html,body{width:1200px;height:1200px;overflow:hidden;background:#fff;font-family:"Poppins",sans-serif;color:var(--ink)}
.page{position:absolute;left:400px;top:0;width:400px;height:1200px;overflow:hidden;background:#fff}
.abs{position:absolute}
.topbar{left:0;top:0;width:400px;height:11px;background:var(--blue)}
.topbar span{position:absolute;top:2.5px;font-size:3.4px;color:#fff;display:flex;align-items:center;gap:2px}
.header{left:0;top:11px;width:400px;height:21px;background:#f4f5f7}
.logo-box{left:65px;top:0;width:50px;height:32px;background:#fff;display:flex;align-items:center;justify-content:center}
.brand{display:flex;align-items:center;gap:2px;font-weight:700;color:var(--blue);font-size:6.6px;letter-spacing:.2px}
.brand i{display:block;width:5px;height:5px;border-radius:50%;background:var(--sky)}
.nav a{position:absolute;top:20px;font-size:3.3px;font-weight:600;color:var(--ink);text-decoration:none}
.btn{position:absolute;display:flex;align-items:center;justify-content:center;gap:1.5px;font-size:3.2px;font-weight:600;background:var(--blue);color:#fff;letter-spacing:.1px}
.btn.ghost{background:#fff;color:var(--blue)}
.hero{left:0;top:32px;width:400px;height:158px;background:linear-gradient(100deg,#1c3550 0%,#3c5a76 35%,#8c9aa8 65%,#c9ced4 85%,#8d98a2 100%)}
.hero-shade{left:0;top:32px;width:400px;height:158px;background:linear-gradient(90deg,rgba(10,30,60,.55),rgba(10,30,60,0) 70%)}
.hero-title{left:65px;top:72px;font-size:15px;line-height:15.5px;font-weight:800;color:#fff}
.hero-text{left:65px;top:112px;font-size:4.3px;line-height:7px;color:#fff}
.dots{left:191px;top:176px;display:flex;gap:2.5px}
.dots i{width:2.5px;height:2.5px;border-radius:50%;border:.5px solid #fff}
.dots i:first-child{background:#fff}
.feature{width:84px;height:47px;top:216px;background:#fff;box-shadow:0 1px 5px rgba(0,0,0,.08)}
.feature .ico{position:absolute;left:6px;top:7px;width:20px;height:20px;border-radius:50%;background:var(--blue);display:flex;align-items:center;justify-content:center}
.feature h3{position:absolute;left:29px;top:7px;font-size:4.2px;font-weight:600}
.feature p{position:absolute;left:29px;top:14.5px;width:52px;font-size:3.1px;line-height:5.5px;color:var(--muted)}
.link{font-size:3.2px;font-weight:600;color:var(--blue)}
.feature .link{position:absolute;left:29px;top:36px}
.eyebrow{font-size:2.7px;letter-spacing:1.2px;color:var(--ink);display:flex;align-items:center;gap:2px;font-weight:500}
.eyebrow i{width:5px;height:5px;border-radius:50%;border:1px solid var(--sky);display:block}
.h2{font-size:10.5px;line-height:12.5px;font-weight:700}
.photo{border-radius:6px}
.about-text{left:178px;top:333px;width:156px;font-size:3.4px;line-height:6.2px;color:var(--muted)}
.list{left:178px;top:359px;list-style:none}
.list li{font-size:3.3px;height:8.3px;display:flex;align-items:center;gap:3px;color:var(--ink)}
.list li i{width:3px;height:3px;border-radius:50%;background:var(--blue);display:block}
.cta{left:0;top:460px;width:400px;height:120px;background:linear-gradient(120deg,#2a2a2a,#3d3d3d 50%,#262626)}
.cta-title{left:0;width:400px;top:493px;text-align:center;color:#fff;font-size:10.5px;line-height:12.5px;font-weight:700}
.services{left:0;top:580px;width:400px;height:222px;background:var(--pale)}
.svc-img{top:655px;width:77px;height:102px}
.svc-card{top:732px;width:68px;height:34px;background:#fff;box-shadow:0 1px 4px rgba(0,0,0,.08)}
.svc-card h4{position:absolute;left:5.5px;top:6px;font-size:4.6px;font-weight:600}
.svc-card p{position:absolute;left:5.5px;top:13px;width:58px;font-size:2.7px;line-height:4.2px;color:var(--muted)}
.svc-card .link{position:absolute;left:5.5px;top:24.5px;font-size:2.9px}
.quote{left:0;top:802px;width:400px;height:50px;background:linear-gradient(110deg,#081a6e 0%,#0b2a8f 45%,#103fb0 70%,#0a2a8e 100%)}
.quote-title{left:65px;top:813px;color:#fff;font-size:11.5px;line-height:14px;font-weight:800;white-space:nowrap}
.quote-sub{left:65px;top:829px;color:#fff;font-size:5.4px;line-height:8px;white-space:nowrap}
.testi{top:937px;width:78px;height:91px;background:#fff;box-shadow:0 1px 5px rgba(0,0,0,.1);border-radius:3px;text-align:center}
.avatar{top:925px;width:24px;height:24px;border-radius:50%;border:1.5px solid #fff;background:radial-gradient(circle,#b89a86,#5d4a40)}
.testi .qm{position:absolute;left:0;width:100%;top:16px;font-size:11px;font-weight:800;line-height:10px}
.testi p{position:absolute;left:5px;width:68px;top:32px;font-size:3.2px;line-height:6.2px;color:var(--ink)}
.testi .stars{position:absolute;left:0;width:100%;top:69px;font-size:3.6px;color:var(--star);letter-spacing:.3px}
.testi .name{position:absolute;left:0;width:100%;top:77px;font-size:4.2px;font-weight:600}
.footer{left:0;top:1040px;width:400px;height:146px}
.fcol h5{font-size:5px;font-weight:600;color:#fff;margin-bottom:5px}
.fcol a{display:block;font-size:3.1px;color:#fff;text-decoration:none;height:8.35px}
.fcol .row{display:flex;gap:3px;font-size:3.1px;color:#fff;line-height:4.6px;margin-bottom:4px}
.social{display:flex;gap:4.5px;left:65px;top:1158px}
.social i{width:6.5px;height:6.5px;border-radius:50%;background:#fff;display:block}
.bottombar{left:0;top:1186px;width:400px;height:14px;background:#073f8d;color:#fff;font-size:3.1px}
</style>
</head>
<body>
<div class="page">

  <div class="abs topbar">
    <span style="left:258px">
      <svg width="4" height="4" viewBox="0 0 24 24" fill="none" stroke="#fff" stroke-width="2"><path d="M22 16.9v3a2 2 0 0 1-2.2 2 19.8 19.8 0 0 1-8.6-3.1 19.5 19.5 0 0 1-6-6A19.8 19.8 0 0 1 2.1 4.2 2 2 0 0 1 4.1 2h3a2 2 0 0 1 2 1.7c.1.9.4 1.8.7 2.7a2 2 0 0 1-.5 2.1L8 9.8a16 16 0 0 0 6 6l1.3-1.3a2 2 0 0 1 2.1-.4c.9.3 1.8.6 2.7.7a2 2 0 0 1 1.7 2z"/></svg>
      (555) 014 2736</span>
    <span style="left:297px">
      <svg width="4" height="4" viewBox="0 0 24 24" fill="none" stroke="#fff" stroke-width="2"><rect x="2" y="4" width="20" height="16" rx="2"/><path d="m2 6 10 7 10-7"/></svg>
      info@corvalenadv.example</span>
  </div>

  <div class="abs header"></div>
  <div class="abs logo-box"><div class="brand"><i></i>Corvalen</div></div>
  <nav class="nav">
    <a style="left:200px">HOME</a>
    <a style="left:220px">SERVICES ▾</a>
    <a style="left:247px">ABOUT</a>
    <a style="left:270px">CONTACT</a>
  </nav>
  <div class="btn" style="left:293px;top:16px;width:40px;height:11px">GET STARTED →</div>

  <div class="abs hero" role="img" aria-label="Photo of a businessman in a suit holding a pen and a tablet at a desk"></div>
  <div class="abs hero-shade"></div>
  <h1 class="abs hero-title">Build Up Your<br>Business Strategy</h1>
  <p class="abs hero-text">Lorem ipsum dolor sit amet, consectetur adipiscing elit,<br>sed do eiusmod tempor incididunt ut labore.</p>
  <div class="btn" style="left:65px;top:139px;width:47px;height:13px">GET STARTED →</div>
  <div class="btn ghost" style="left:119px;top:139px;width:47px;height:13px">EXPLORE MORE →</div>
  <div class="abs dots"><i></i><i></i><i></i><i></i></div>

  <div class="abs feature" style="left:65px">
    <div class="ico"><svg width="10" height="10" viewBox="0 0 24 24" fill="none" stroke="#fff" stroke-width="1.6"><rect x="3" y="4" width="18" height="13" rx="1"/><path d="M7 13l3-3 3 2 4-4M9 21h6M12 17v4"/></svg></div>
    <h3>Business Strategy</h3>
    <p>Lorem ipsum dolor sit amet, consectetur adipiscing elit, sed do eiusmod tempor.</p>
    <span class="link">Get Started →</span>
  </div>
  <div class="abs feature" style="left:157px">
    <div class="ico"><svg width="10" height="10" viewBox="0 0 24 24" fill="none" stroke="#fff" stroke-width="1.6"><rect x="5" y="3" width="14" height="18" rx="1"/><path d="M8 7h8M8 11h2M12 11h2M8 15h2M12 15h2M8 18h8"/></svg></div>
    <h3>Financial Planning</h3>
    <p>Lorem ipsum dolor sit amet, consectetur adipiscing elit, sed do eiusmod tempor.</p>
    <span class="link">Get Started →</span>
  </div>
  <div class="abs feature" style="left:249px">
    <div class="ico"><svg width="10" height="10" viewBox="0 0 24 24" fill="none" stroke="#fff" stroke-width="1.6"><path d="M4 21V11h4v10M10 21V7h4v14M16 21v-6h4v6M3 21h18"/><circle cx="17" cy="6" r="3"/></svg></div>
    <h3>Wealth Management</h3>
    <p>Lorem ipsum dolor sit amet, consectetur adipiscing elit, sed do eiusmod tempor.</p>
    <span class="link">Get Started →</span>
  </div>

  <div class="abs photo" style="left:65px;top:289px;width:95px;height:135px;background:linear-gradient(160deg,#e9ecef 0%,#cfd8e0 40%,#2f7fb3 75%,#d7dbe0 100%)" role="img" aria-label="Photo of a bar chart report being examined with a magnifying glass"></div>
  <div class="abs photo" style="left:111px;top:358px;width:57px;height:72px;border:2.5px solid #fff;background:linear-gradient(150deg,#b9c6d3,#3f5a78 55%,#d9d9d9)" role="img" aria-label="Photo of two colleagues discussing work over a laptop"></div>

  <div class="abs eyebrow" style="left:178px;top:291px"><i></i>KNOW MORE ABOUT US</div>
  <h2 class="abs h2" style="left:178px;top:300px">We Provide<br>Best Business Solution</h2>
  <p class="abs about-text">Lorem ipsum dolor sit amet, consectetur adipiscing elit, sed do eiusmod tempor incid-idunt ut labore et dolore magna aliqua. Quis ipsum suspendisse ultrices gravida. Risus commodo viverra maecenas accumsan lacus vel facilisis.</p>
  <ul class="abs list">
    <li><i></i>Lorem Ipsum is simply dummy text</li>
    <li><i></i>Lorem Ipsum has been the industry</li>
    <li><i></i>Standard dummy text ever since the</li>
    <li><i></i>When an unknown printer took a galley</li>
    <li><i></i>Scrambled it to make a type specimen book</li>
  </ul>
  <div class="btn" style="left:178px;top:409px;width:47px;height:13px">GET STARTED →</div>

  <div class="abs cta" role="img" aria-label="Photo of a team meeting around a table in an office, shown in greyscale"></div>
  <h2 class="abs cta-title">Let’s discuss about how we can help<br>make your business better</h2>
  <div class="btn" style="left:166px;top:533px;width:59px;height:13px">LET’S WORK TOGETHER →</div>

  <div class="abs services"></div>
  <div class="abs eyebrow" style="left:65px;top:604px"><i></i>OUR SERVICES</div>
  <h2 class="abs h2" style="left:65px;top:612px">Best Solutions<br>For Your Business</h2>
  <div class="btn" style="left:286px;top:622px;width:47px;height:13px">ALL SERVICES →</div>

  <div class="abs svc-img" style="left:65px;background:linear-gradient(135deg,#c99a3a,#e4c06b 45%,#3b4a5f)" role="img" aria-label="Photo of people reviewing charts on a yellow table"></div>
  <div class="abs svc-img" style="left:148px;background:linear-gradient(135deg,#6d5a4a,#c7b08d 45%,#e06c9a 80%,#e8dc5a)" role="img" aria-label="Photo of hands arranging sticky notes and prints for planning"></div>
  <div class="abs svc-img" style="left:231px;background:linear-gradient(135deg,#e9e4dc,#c9c4bb 50%,#4b4b4b)" role="img" aria-label="Photo of hands pointing at printed analysis charts"></div>
  <div class="abs svc-img" style="left:315px;background:linear-gradient(135deg,#a9a9a9,#7d8da2 50%,#d9d2c6)" role="img" aria-label="Photo of a consultant advising a client at a table"></div>

  <div class="abs svc-card" style="left:65px"><h4>Business Planning</h4><p>Lorem ipsum dolor sit donec amet tristique ante vel sem.</p><span class="link">Get Started →</span></div>
  <div class="abs svc-card" style="left:148px"><h4>Strategy &amp; Planning</h4><p>Lorem ipsum dolor sit donec amet tristique ante vel sem.</p><span class="link">Get Started →</span></div>
  <div class="abs svc-card" style="left:231px"><h4>Audit &amp; Evaluation</h4><p>Lorem ipsum dolor sit donec amet tristique ante vel sem.</p><span class="link">Get Started →</span></div>
  <div class="abs svc-card" style="left:315px"><h4>Consultancy &amp; Advice</h4><p>Lorem ipsum dolor sit donec amet tristique ante vel sem.</p><span class="link">Get Started →</span></div>

  <div class="abs quote"></div>
  <h2 class="abs quote-title">Get a Free Quote Today!</h2>
  <p class="abs quote-sub">Perfect solution for your business</p>
  <div class="btn ghost" style="left:286px;top:820px;width:47px;height:13px">CONTACT US →</div>

  <div class="abs eyebrow" style="left:182px;top:881px"><i></i>TESTIMONIALS</div>
  <h2 class="abs h2" style="left:0;width:400px;text-align:center;top:889px">What People Say About Us</h2>

  <div class="abs testi" style="left:67px"><div class="qm">”</div><p>Lorem Ipsum is simply dummy text of the printing and typesetting industry. Lorem Ipsum has been the industry's standard dummy text ever since the 1500s.</p><div class="stars">★★★★★</div><div class="name">Dana Whitfield</div></div>
  <div class="abs testi" style="left:160px"><div class="qm">”</div><p>Lorem Ipsum is simply dummy text of the printing and typesetting industry. Lorem Ipsum has been the industry's standard dummy text ever since the 1500s.</p><div class="stars">★★★★★</div><div class="name">Marco</div></div>
  <div class="abs testi" style="left:255px"><div class="qm">”</div><p>Lorem Ipsum is simply dummy text of the printing and typesetting industry. Lorem Ipsum has been the industry's standard dummy text ever since the 1500s.</p><div class="stars">★★★★★</div><div class="name">Idris</div></div>
  <div class="abs avatar" style="left:94px" role="img" aria-label="Portrait of client Dana Whitfield"></div>
  <div class="abs avatar" style="left:187px" role="img" aria-label="Portrait of client Marco"></div>
  <div class="abs avatar" style="left:282px" role="img" aria-label="Portrait of client Idris"></div>

  <svg class="abs footer" viewBox="0 0 400 146" preserveAspectRatio="none" aria-hidden="true">
    <path d="M0 10 C60 -8 120 30 200 40 C280 50 330 40 400 13 L400 146 L0 146 Z" fill="var(--blue)"/>
    <path d="M300 50 C340 44 380 30 400 20 L400 24 C370 40 340 48 300 52 Z" fill="#ffffff" opacity=".9"/>
  </svg>

  <div class="abs brand" style="left:65px;top:1113px;color:#fff;font-size:7.5px"><i style="background:#fff"></i>Corvalen</div>
  <p class="abs" style="left:65px;top:1132px;width:62px;font-size:3.1px;line-height:5.5px;color:#fff">Nemo enim ipsam voluptatem quia voluptas sit aspernatur aut odit aut fugit sed quia consequuntu.</p>
  <div class="abs social"><i></i><i></i><i></i></div>

  <div class="abs fcol" style="left:168px;top:1112px"><h5>Quick Links</h5><a>Home</a><a>Services</a><a>About</a><a>Contact</a></div>
  <div class="abs fcol" style="left:225px;top:1112px"><h5>Our Services</h5><a>Business Planning</a><a>Strategy &amp; Planning</a><a>Audit &amp; Evaluation</a><a>Consultancy &amp; Advice</a><a>Develop Process</a><a>Business Support</a></div>
  <div class="abs fcol" style="left:290px;top:1112px"><h5>Contact Us</h5>
    <div class="row"><svg width="4" height="4" viewBox="0 0 24 24" fill="none" stroke="#fff" stroke-width="2"><path d="M12 22s7-6.5 7-12a7 7 0 0 0-14 0c0 5.5 7 12 7 12z"/><circle cx="12" cy="10" r="2.5"/></svg><span>82 Harbor Ln, Springfield,<br>VA 22150, USA</span></div>
    <div class="row"><svg width="4" height="4" viewBox="0 0 24 24" fill="none" stroke="#fff" stroke-width="2"><path d="M22 16.9v3a2 2 0 0 1-2.2 2A19.8 19.8 0 0 1 2.1 4.2 2 2 0 0 1 4.1 2h3l2 5-2.5 1.5a11 11 0 0 0 6 6L15 12l5 2z"/></svg><span>(555) 014 2736</span></div>
    <div class="row"><svg width="4" height="4" viewBox="0 0 24 24" fill="none" stroke="#fff" stroke-width="2"><rect x="2" y="4" width="20" height="16" rx="2"/><path d="m2 6 10 7 10-7"/></svg><span>info@corvalenadv.example</span></div>
  </div>

  <div class="abs bottombar">
    <span class="abs" style="left:65px;top:5px">Copyright © 2024, Corvalen Advisory Partners. All Rights Reserved.</span>
    <span class="abs" style="right:67px;top:5px">Terms &amp; Conditions &nbsp;|&nbsp; Privacy Policy</span>
  </div>
</div>
</body>
</html>
```